WordPress Coding + Design - Website designed to maximise leads required

Please see the velmot brief.doc file

it is VERY important that this website be DESIGNED with MOBILE + TABLET BOOTSTRAP in mind.

The design has to look amazing on mobile and tablet.

Reason: Designer failed to meet expectations and wasted my time

Number of Pages Required

1 page

```html
<!DOCTYPE html>
<html lang="en">
<head>
<meta charset="utf-8">
<title>Velmot College Advisors</title>
<link href="https://fonts.googleapis.com/css2?family=Roboto:wght@300;400;500;700&display=swap" rel="stylesheet">
<style>
:root{
  --navy:#1f2a7c;
  --gold:#b8862b;
  --gold-light:#c99a3d;
  --text:#555a60;
  --heading:#3a3d42;
  --light:#f1f1f1;
  --white:#ffffff;
  --play:#3a3a3a;
}
*{margin:0;padding:0;box-sizing:border-box}
html,body{width:1200px;height:2848px;overflow:hidden}
body{font-family:'Roboto',Arial,sans-serif;color:var(--text);background:var(--white);position:relative}
section,header,footer,nav{position:absolute;left:0;width:1200px}
.abs{position:absolute}
.center{left:0;width:1200px;text-align:center}

.top-rule{top:0;height:8px;background:var(--navy)}
.site-header{top:8px;height:100px;background:var(--white)}
.brand{left:80px;top:20px;display:flex;align-items:center;gap:10px}
.brand-mark{width:62px;height:62px;border-radius:50%;background:var(--navy)}
.brand-name{font-size:30px;font-weight:700;color:var(--navy);line-height:1}
.brand-url{font-size:13px;font-weight:700;color:var(--navy);margin-top:4px;letter-spacing:.5px}
.header-links{right:80px;top:50px;font-size:14px;color:var(--navy)}
.header-links span{margin:0 14px}

.main-nav{top:108px;height:54px;background:var(--gold)}
.main-nav ul{list-style:none;display:flex;position:absolute;left:95px;top:12px;gap:0}
.main-nav li{font-size:14px;color:var(--white);height:32px;line-height:32px;padding:0 14px;margin-right:8px}
.main-nav li.active{background:var(--navy)}

.hero{top:162px;height:402px;background:linear-gradient(100deg,#4a3e48 0%,#8a6d6a 35%,#b09088 60%,#6e5a60 100%)}
.hero-title{top:130px;font-size:42px;font-weight:500;color:var(--white)}
.hero-sub{top:190px;font-size:26px;font-weight:300;color:#e0b25a}
.btn-gold{background:var(--gold);color:var(--white);font-weight:500;font-size:16px;text-align:center}
.hero-btn{left:475px;top:247px;width:248px;height:44px;line-height:44px;background:rgba(184,134,43,.9)}
.hero-dots{top:364px;display:flex;justify-content:center;gap:14px}
.hero-dots i{width:14px;height:14px;border-radius:50%;border:2px solid var(--white)}
.hero-dots i.on{background:var(--white)}

.welcome{top:564px;height:300px}
.section-title{font-size:22px;font-weight:500;color:var(--heading);letter-spacing:.5px}
.welcome .section-title{top:40px}
.welcome-divider{left:370px;top:78px}
.gold-sub{font-size:24px;color:var(--gold);font-weight:400}
.welcome .gold-sub{top:110px}
.welcome-text{left:220px;width:760px;top:156px;font-size:14px;line-height:24px;text-align:center}
.btn-navy{background:var(--navy);color:var(--white);font-size:15px;text-align:center}
.welcome .btn-navy{left:524px;top:226px;width:152px;height:34px;line-height:34px}

.universities{top:864px;height:123px;background:linear-gradient(#e2e2e2,#fff 18%,#fff 82%,#e2e2e2)}
.universities-text{left:80px;top:52px;font-size:18px;font-weight:500;color:var(--navy)}
.list-btn{left:803px;top:36px}

.services{top:987px;height:430px;background:linear-gradient(90deg,#3d3c40 0%,#6f5e56 40%,#5a4c48 70%,#3a3a3e 100%)}
.services .section-title{top:42px;color:var(--white)}
.dash{border-top:2px dashed var(--gold-light);width:210px;left:495px}
.services .dash{top:82px}
.service-card{top:133px;width:244px;height:251px;background:rgba(184,134,43,.85);color:var(--white);text-align:center}
.service-card svg{margin-top:30px}
.service-name{font-size:19px;margin-top:14px}
.service-line{width:150px;border-top:1px solid rgba(255,255,255,.6);margin:8px auto 12px}
.service-card p{font-size:12.5px;line-height:21px}
.slide-arrow{top:233px;width:50px;height:42px;background:var(--gold);display:flex;align-items:center;justify-content:center}

.about{top:1417px;height:415px}
.about .section-title{top:34px}
.about .dash{top:76px;border-color:#999;width:210px}
.about .gold-sub{top:102px}
.thumb{left:80px;width:146px;background:linear-gradient(135deg,#5a3a2e,#8c6b5a,#3c2d2a)}
.thumb-1{top:165px;height:95px;border:3px solid var(--gold)}
.thumb-2{top:275px;height:93px;background:linear-gradient(135deg,#3a3c5e,#7b6a70,#2d2c3e)}
.video{left:254px;top:165px;width:342px;height:201px;background:linear-gradient(135deg,#2b2b2b,#6a5040 45%,#3c5a3a 80%,#222)}
.video-caption{left:10px;top:6px;font-size:13px;color:var(--white)}
.video-play{left:150px;top:80px}
.video-bar{left:0;bottom:0;width:342px;height:30px;background:#111;color:#ddd;font-size:11px;padding:8px 0 0 50px}
.about-text{left:650px;top:166px;width:470px;height:164px;overflow:hidden;font-size:12px;line-height:27px;text-align:right}
.about .btn-navy{left:968px;top:342px;width:152px;height:34px;line-height:34px}

.audio{top:1832px;height:124px;background:linear-gradient(90deg,#d8d8d8,#f7f7f7 12%,#fff 50%,#f7f7f7 88%,#d8d8d8)}
.player{top:25px;width:204px;height:74px;background:var(--white);border:3px solid #a8873e;border-radius:3px}
.player-play{left:12px;top:16px;width:28px;height:28px;border-radius:50%;background:#d6d6d6}
.player-meta{left:50px;top:12px;font-size:11px;color:#666}
.player-meta b{display:block;font-size:12px;color:#333;font-weight:500;margin-top:3px}
.player-track{left:12px;bottom:8px;width:174px;height:2px;background:#ddd}

.partners{top:1956px;height:262px;background:#eeeeee}
.partners .section-title{top:40px}
.partners .dash{top:82px}
.partner{top:129px;width:188px;height:89px;background:var(--white);border:1px solid #ddd}
.partner-badge{left:54px;top:20px;width:80px;height:48px;background:#cfcfcf;border-radius:4px}
.circle-arrow{top:156px;width:30px;height:30px;border-radius:50%;background:#8d8d8d}

.testimonials{top:2218px;height:266px;background:linear-gradient(90deg,#2d2a26 0%,#5a4a3c 35%,#7a6552 50%,#4a4034 75%,#2a2824 100%)}
.testimonials-title{left:110px;top:110px;font-size:30px;font-weight:300;color:var(--white)}
.testimonials-rule{left:100px;top:155px;width:176px;border-top:2px dashed var(--gold-light)}
.quote-box{left:604px;top:65px;width:493px;height:140px;background:rgba(184,134,43,.85);color:var(--white);padding:16px 22px}
.quote-name{font-size:15px;padding-bottom:12px;border-bottom:1px solid rgba(255,255,255,.5)}
.quote-text{font-size:12.5px;font-style:italic;line-height:23px;margin-top:14px}

.contact{top:2484px;height:313px}
.contact-title{left:80px;top:44px;font-size:21px;font-weight:400;color:var(--heading)}
.map{left:80px;top:85px;width:345px;height:179px;background:linear-gradient(135deg,#e8e4dc,#d4dcc8 45%,#cfd9e4);border:3px solid #ccc}
.address{left:461px;top:85px;width:219px;height:152px;background:var(--gold);color:var(--white);font-size:13px;line-height:22px;padding:14px 22px}
.address-pointer{left:429px;top:97px}
.contact-divider{left:773px;top:47px;height:213px;border-left:1px solid #ccc}
.newsletter-title{left:860px;top:44px;font-size:21px;font-weight:400;color:var(--heading)}
.newsletter-text{left:860px;top:82px;width:260px;font-size:13px;line-height:26px;color:var(--gold)}
.email{left:860px;top:146px;width:258px;height:40px;border:1px solid #ccc;font-size:13px;color:#999;padding:11px 14px}
.subscribe{left:864px;top:209px;width:102px;height:30px;line-height:30px;font-size:13px}

.site-footer{top:2797px;height:51px;background:var(--navy)}
.footer-copy{left:80px;top:18px;font-size:12px;color:var(--white)}
.social{top:10px;width:30px;height:30px;background:#3a6fd0;border-radius:3px}
</style>
</head>
<body>

<div class="abs top-rule" style="left:0;width:1200px"></div>

<header class="site-header">
  <div class="abs brand">
    <div class="brand-mark"></div>
    <div>
      <div class="brand-name">Velmot College Advisors</div>
      <div class="brand-url">www.velmotnet.com</div>
    </div>
  </div>
  <div class="abs header-links">Student Portal Login<span>|</span>Sign Up for Newsletter</div>
</header>

<nav class="main-nav">
  <ul>
    <li class="active">Home</li><li>About</li><li>Students</li><li>Our Team</li><li>Services</li><li>Media</li><li>FAQ</li><li>Links</li><li>Events</li><li>Location</li>
  </ul>
</nav>

<section class="hero" role="img" aria-label="Photo of smiling students pointing forward in front of an American flag">
  <h1 class="abs center hero-title">Create your future with us!</h1>
  <p class="abs center hero-sub">We Guide and Empower Students</p>
  <div class="abs btn-gold hero-btn">Request for Free Consultation</div>
  <div class="abs center hero-dots"><i class="on"></i><i></i><i></i></div>
</section>

<section class="welcome">
  <h2 class="abs center section-title">WELCOME TO VELMOT COLLEGE ADVISORS</h2>
  <svg class="abs welcome-divider" width="460" height="26" viewBox="0 0 460 26">
    <line x1="0" y1="13" x2="205" y2="13" stroke="#b8862b" stroke-width="2" stroke-dasharray="4 3"/>
    <line x1="255" y1="13" x2="460" y2="13" stroke="#b8862b" stroke-width="2" stroke-dasharray="4 3"/>
    <circle cx="230" cy="13" r="12" fill="#1f2a7c"/>
  </svg>
  <p class="abs center gold-sub">Your US University Specialists in the GCC</p>
  <p class="abs welcome-text">When you engage us, you have access to an entire team of American university professionals with relevant firsthand admissions experience, education, and...</p>
  <div class="abs btn-navy">Read More</div>
</section>

<section class="universities">
  <p class="abs universities-text">UNIVERSITIES TO WHICH OURSTUDENTS HAVE BEEN ADMITTED(PARTIAL LIST)</p>
  <svg class="abs list-btn" width="317" height="46" viewBox="0 0 317 46">
    <polygon points="0,0 317,0 297,23 317,46 0,46 20,23" fill="#b8862b"/>
    <polygon points="0,0 40,0 40,46 0,46 20,23" fill="#a57725"/>
    <polygon points="277,0 317,0 297,23 317,46 277,46" fill="#a57725"/>
    <text x="138" y="30" font-family="Roboto, Arial, sans-serif" font-size="21" fill="#fff" text-anchor="middle">Check the list</text>
    <rect x="225" y="15" width="15" height="15" fill="none" stroke="#fff" stroke-width="2"/>
    <polyline points="228,21 233,26 243,13" fill="none" stroke="#fff" stroke-width="2.5"/>
  </svg>
</section>

<section class="services" role="img" aria-label="Background photo of a smiling student">
  <h2 class="abs center section-title">OUR SERVICES</h2>
  <div class="abs dash"></div>
  <div class="abs slide-arrow" style="left:0"><svg width="14" height="20"><polyline points="10,3 3,10 10,17" fill="none" stroke="#fff" stroke-width="2.5"/></svg></div>
  <div class="abs slide-arrow" style="left:1150px"><svg width="14" height="20"><polyline points="4,3 11,10 4,17" fill="none" stroke="#fff" stroke-width="2.5"/></svg></div>

  <div class="abs service-card" style="left:129px">
    <svg width="56" height="64" viewBox="0 0 56 64"><circle cx="34" cy="8" r="6" fill="#fff"/><path d="M18 20 L36 18 L30 38 L40 56 L34 58 L24 42 L16 58 L10 55 L20 36 L24 26 L16 28 Z" fill="#fff"/><circle cx="44" cy="54" r="6" fill="none" stroke="#fff" stroke-width="2"/></svg>
    <div class="service-name">Sports Package</div>
    <div class="service-line"></div>
    <p>15 Academic Counselling Sessions<br>Unlimited Highlight Video Editing<br>Promotion and Communic.....</p>
  </div>
  <div class="abs service-card" style="left:478px">
    <svg width="76" height="64" viewBox="0 0 76 64"><circle cx="38" cy="14" r="9" fill="#fff"/><circle cx="16" cy="22" r="7" fill="#fff"/><circle cx="60" cy="22" r="7" fill="#fff"/><path d="M24 58 Q24 28 38 28 Q52 28 52 58 Z" fill="#fff"/><path d="M4 58 Q4 34 16 34 Q24 34 24 44 L22 58 Z" fill="#fff"/><path d="M72 58 Q72 34 60 34 Q52 34 52 44 L54 58 Z" fill="#fff"/></svg>
    <div class="service-name">Crimson Package</div>
    <div class="service-line"></div>
    <p>One-on-One Counseling<br>Up to 12 Applications<br>Multiple Personal Statement ......</p>
  </div>
  <div class="abs service-card" style="left:826px">
    <svg width="60" height="64" viewBox="0 0 60 64"><circle cx="30" cy="22" r="16" fill="none" stroke="#fff" stroke-width="5"/><path d="M6 62 Q6 42 30 42 Q54 42 54 62 Z" fill="#fff"/></svg>
    <div class="service-name">IVY Package</div>
    <div class="service-line"></div>
    <p>One-on-One Counseling<br>Up to 8 Applications<br>Multiple Personal Statement ......</p>
  </div>
</section>

<section class="about">
  <h2 class="abs center section-title">ABOUT US</h2>
  <div class="abs dash"></div>
  <p class="abs center gold-sub">We are independent educational consultants - Not agents</p>
  <div class="abs thumb thumb-1" role="img" aria-label="Video thumbnail of an interview"></div>
  <div class="abs thumb thumb-2" role="img" aria-label="Video thumbnail about studying in the United States"></div>
  <div class="abs video" role="img" aria-label="Video still of Peter Halden interviewed on Lumen Weekly">
    <div class="abs video-caption">Lumen Weekly- Interview Featuring Peter Halden...</div>
    <svg class="abs video-play" width="42" height="42" viewBox="0 0 42 42"><circle cx="21" cy="21" r="20" fill="var(--play)" fill-opacity=".75"/><polygon points="16,12 30,21 16,30" fill="#fff"/></svg>
    <div class="abs video-bar">0:00 / 11:13</div>
  </div>
  <p class="abs about-text">We are not commissioned agents working on behalf of any universities. Our commitment is to our students and finding/applying to the best universities for their academic and professional goals. Applying to US universities is a holistic process, which typically involves the submission of a personal statement, supplemental essays, standardized test scores, academic transcripts, letters of recommendation, summary list of extracurricular activities, description of past summer ........</p>
  <div class="abs btn-navy">Read More</div>
</section>

<section class="audio">
  <div class="abs player" style="left:100px"><div class="abs player-play"></div><div class="abs player-meta">Cityeye<b>Education Matters 5, 20...</b></div><div class="abs player-track"></div></div>
  <div class="abs player" style="left:366px"><div class="abs player-play"></div><div class="abs player-meta">Cityeye<b>Education Matters 5, 20...</b></div><div class="abs player-track"></div></div>
  <div class="abs player" style="left:630px"><div class="abs player-play"></div><div class="abs player-meta">Cityeye<b>Education Matters 5, 20...</b></div><div class="abs player-track"></div></div>
  <div class="abs player" style="left:894px"><div class="abs player-play"></div><div class="abs player-meta">Cityeye<b>Education Matters 5, 20...</b></div><div class="abs player-track"></div></div>
</section>

<section class="partners">
  <h2 class="abs center section-title">PARTNERS</h2>
  <div class="abs dash"></div>
  <div class="abs circle-arrow" style="left:28px"><svg width="30" height="30"><polyline points="17,9 11,15 17,21" fill="none" stroke="#fff" stroke-width="2.5"/></svg></div>
  <div class="abs circle-arrow" style="left:1142px"><svg width="30" height="30"><polyline points="13,9 19,15 13,21" fill="none" stroke="#fff" stroke-width="2.5"/></svg></div>
  <div class="abs partner" style="left:135px"><div class="abs partner-badge"></div></div>
  <div class="abs partner" style="left:383px"><div class="abs partner-badge"></div></div>
  <div class="abs partner" style="left:632px"><div class="abs partner-badge"></div></div>
  <div class="abs partner" style="left:881px"><div class="abs partner-badge"></div></div>
</section>

<section class="testimonials" role="img" aria-label="Background photo of a graduate in cap and gown">
  <h2 class="abs testimonials-title">Testimonials</h2>
  <div class="abs testimonials-rule"></div>
  <div class="abs quote-box">
    <div class="quote-name">Mark Ellison-Ray</div>
    <p class="quote-text">“ Nam liber tempor cum soluta nobis eleifend opti on congue nihil imperdiet doming id quod mazim placerat facer possim assum. Typi non habent claritatem ”</p>
  </div>
</section>

<section class="contact">
  <h2 class="abs contact-title">CONTACT US</h2>
  <div class="abs map" role="img" aria-label="Street map showing the office location"></div>
  <svg class="abs address-pointer" width="34" height="36"><polygon points="34,0 34,36 0,18" fill="#b8862b"/></svg>
  <div class="abs address">No 4, Harbor Crest Building,<br>Palm Coast Road,<br>Dubai, UAE<br><span style="display:block;margin-top:8px">Tel: +971 4 555 0142</span>info@velmotnet.com</div>
  <div class="abs contact-divider"></div>
  <h2 class="abs newsletter-title">NEWSLETTER</h2>
  <p class="abs newsletter-text">Sign Up forSubscribing updates Lorem Ipsum dolore set epsum</p>
  <div class="abs email">Email Address</div>
  <div class="abs btn-navy subscribe">Subscribe</div>
</section>

<footer class="site-footer">
  <p class="abs footer-copy">Velmot College Advisors © 2015 | Privacy policy</p>
  <div class="abs social" style="left:995px"></div>
  <div class="abs social" style="left:1043px;background:#4aa3df"></div>
  <div class="abs social" style="left:1091px;background:#c4302b"></div>
</footer>

</body>
</html>
```